Web Design Project

Current website needs stylish revamping www.trel-ika.com!!!! The look and font should be playful while showing maybe wings, shoes or something that is sexy yet confident for women to wear. The line is a division of a larger company and trademarked under their umbrella entity.

The website should have a clean, trendy and possibly modern look. Important project with hopeful long term business relation ship.

The slogan is also playful...
brr-ivo - made to glide, never pause
or
brr-ivo, quick in the stride (hence the idea of wings in the title or website)

brr-ivo...., shh, shoes be seen, not heard, light, ect.
Updates

Payment is now guaranteed- we appreciate your work!!!!

Would also like a possible slide show for the home page!!

Not many designs submitted!!! so design away - thank you greatly :)

Kindest regards,
NormaĀ 

Reason: need a great design for this project- appreciate your help!

Elegant sexy, not trashy!!!

also more clean, sophisticated and modern look- not too busy!!!
clients are high end
thank you so much!!
NormaĀ 

Target Market(s)

successful, working women

Industry/Entity Type

Business

Requirements
Must have
• Must be clean, buyer and user friendly and embody a sexy feel. Possibly bold colors or mix of neutral beige with black.

```html
<!DOCTYPE html>
<html lang="en">
<head>
<meta charset="utf-8">
<title>brr-ivo — Home</title>
<link rel="stylesheet" href="https://fonts.googleapis.com/css2?family=Roboto+Condensed:wght@300;400&family=Arimo:wght@400&display=swap">
<style>
:root{
  --ink:#1f1f1f;
  --muted:#555;
  --plum:#5a2b88;
  --rose:#e2125f;
  --rule:#2a2a2a;
  --soft:#d9d9d9;
  --paper:#ffffff;
  --card-line:#cfcfcf;
}
*{box-sizing:border-box;margin:0;padding:0}
html,body{width:1128px;height:1200px;overflow:hidden;background:var(--paper)}
body{font-family:"Roboto Condensed",sans-serif;color:var(--ink);position:relative}
a{color:inherit;text-decoration:none}
.abs{position:absolute}

/* header */
.brand{left:132px;top:12px}
.brand-name{font-size:56px;font-weight:400;letter-spacing:-1px;line-height:1;color:var(--ink)}
.brand-tag{font-size:13px;font-weight:300;color:var(--muted);margin-top:2px}
.account-links{right:132px;top:18px;font-size:12.5px;color:var(--plum)}
.account-links span{margin:0 7px;color:var(--muted)}
.cart{left:652px;top:56px;font-family:"Arimo",sans-serif;font-size:11.5px;color:var(--plum)}
.cart-total{left:676px;top:79px;font-size:13.5px;color:var(--plum)}
.cart-checkout{left:734px;top:80px;font-size:12.5px;color:var(--rose)}
.cart-divider{left:799px;top:56px;width:1px;height:38px;background:var(--soft)}
.search{left:820px;top:55px;width:176px;height:27px;border:2px solid var(--soft);border-radius:14px;font-family:"Arimo",sans-serif;font-size:11px;color:#666;padding:5px 9px}
.search svg{position:absolute;right:9px;top:5px}
.search-links{right:132px;top:88px;font-family:"Arimo",sans-serif;font-size:11px;color:var(--plum)}
.search-links span{margin:0 6px;color:var(--muted)}

/* nav */
.nav{left:0;top:114px;width:1128px;height:37px;border-top:1px solid var(--rule);border-bottom:1px solid var(--rule)}
.nav ul{list-style:none;position:absolute;left:150px;top:9px;display:flex;font-size:16px;text-transform:uppercase}
.nav li{margin-right:43px}
.nav li.active{color:var(--plum)}

/* hero slideshow */
.hero{left:132px;top:160px;width:862px;height:340px;background:linear-gradient(90deg,#1a1a22 0%,#2a2a33 30%,#1b1b22 100%)}
.hero-photo{position:absolute;inset:0;background:radial-gradient(ellipse at 30% 55%,#b4b1ab 0%,#8f8c86 22%,transparent 45%),radial-gradient(ellipse at 72% 40%,#aaa7a1 0%,#8d8a84 25%,transparent 48%)}
.hero-arrows{position:absolute;right:8px;bottom:10px;display:flex;gap:8px}
.hero-arrows span{width:21px;height:19px;background:#e8e8e8;border-radius:4px;display:flex;align-items:center;justify-content:center}

/* style chooser */
.style-btn{left:132px;top:514px;width:141px;height:30px;background:var(--rose);border-radius:15px;color:#fff;font-size:15px;padding:5px 12px}
.style-btn svg{position:absolute;right:16px;top:12px}

/* product grid */
.card{width:178px;height:196px;border:1px solid var(--card-line);background:#fff}
.card::after{content:"";position:absolute;right:-20px;top:40px;width:18px;height:156px;background:linear-gradient(90deg,rgba(0,0,0,.18),rgba(0,0,0,0));transform:skewY(-8deg);transform-origin:top left}
.shot{position:absolute;left:14px;top:8px;width:150px;height:150px}
.shot-black{background:radial-gradient(ellipse at 50% 50%,#111 0%,#222 38%,#fff 66%)}
.shot-suede{background:radial-gradient(ellipse at 50% 60%,#1a1a1a 0%,#2b2b2b 34%,#f4f4f4 64%)}
.shot-gold{background:radial-gradient(ellipse at 50% 50%,#d6a94a 0%,#c08d2e 30%,#6a5a38 45%,#fff 66%)}
.shot-beige{background:radial-gradient(ellipse at 50% 55%,#1c1c1c 0%,#c9b6a2 36%,#d7c6b3 48%,#fff 68%)}
.price{width:58px;height:58px;border-radius:50%;background:#fff;box-shadow:0 2px 5px rgba(0,0,0,.25);color:var(--rose);font-size:15px;display:flex;align-items:center;justify-content:center}
.action{font-size:14px;color:#333;text-transform:uppercase}

/* footer */
.footer-rule{left:0;top:1065px;width:1128px;height:1px;background:var(--soft)}
.foot-links{left:132px;top:1077px;font-family:"Arimo",sans-serif;font-size:11.5px;color:var(--muted);line-height:20.3px}
.foot-head{font-size:14px;color:var(--rose);text-transform:uppercase}
.newsletter-input{left:348px;top:1094px;width:187px;height:21px;border:1px solid #bbb;border-radius:3px}
.subscribe{left:348px;top:1124px;width:57px;height:21px;background:#e4e4e4;border-radius:4px;font-size:13px;text-align:center;line-height:21px}
.payments{left:581px;top:1104px;display:flex;gap:8px;font-family:"Arimo",sans-serif;font-size:10px;color:var(--plum)}
.payments span{display:flex;align-items:center;gap:3px;white-space:nowrap}
.payments i{width:7px;height:7px;background:var(--plum);display:inline-block}
.social{left:781px;top:1106px;display:flex;gap:11px;font-family:"Arimo",sans-serif;font-size:10px;color:var(--plum)}
.social span{display:flex;flex-direction:column;align-items:center;gap:3px}
.social i{width:18px;height:18px;border-radius:50%;background:var(--rose);display:block}
.legal{left:132px;top:1168px;font-family:"Arimo",sans-serif;font-size:11px;color:var(--muted)}
.legal span{margin:0 6px}
</style>
</head>
<body>

<header>
  <div class="abs brand">
    <div class="brand-name">brr-ivo</div>
    <div class="brand-tag">brr-ivo - made to glide, never pause</div>
  </div>
  <nav class="abs account-links"><a href="#">My Account</a><span>/</span><a href="#">Order Status</a><span>/</span><a href="#">Wish Lists</a><span>/</span><a href="#">Gift Certificates</a></nav>

  <div class="abs cart">
    <svg width="16" height="16" viewBox="0 0 16 16" style="vertical-align:-3px;margin-right:4px" aria-hidden="true"><path d="M1 2h3l2 8h8l1.5-6H5" fill="none" stroke="#5a78c8" stroke-width="1.6"/><circle cx="7" cy="13" r="1.4" fill="#5a78c8"/><circle cx="13" cy="13" r="1.4" fill="#5a78c8"/></svg>2 Items In your cart
  </div>
  <div class="abs cart-total">$68.00</div>
  <a class="abs cart-checkout" href="#">CHECKOUT</a>
  <div class="abs cart-divider"></div>

  <div class="abs search">Search
    <svg width="15" height="15" viewBox="0 0 15 15" aria-hidden="true"><circle cx="6" cy="6" r="4.3" fill="none" stroke="#333" stroke-width="1.6"/><path d="M9.2 9.2l4.3 4.3" stroke="#333" stroke-width="2.2"/></svg>
  </div>
  <div class="abs search-links"><a href="#">Advanced Search</a><span>/</span><a href="#">Search Tips</a></div>

  <nav class="abs nav">
    <ul>
      <li class="active">Home</li><li>Collections</li><li>No More Noise</li><li>About Us</li><li>Reviews</li><li>Blog</li><li>Press</li><li>Store</li><li style="margin-right:0">Contact</li>
    </ul>
  </nav>
</header>

<main>
  <section class="abs hero">
    <div class="hero-photo" role="img" aria-label="Slideshow photo: pair of grey studded peep-toe platform heels with bows on a dark cloth"></div>
    <div class="hero-arrows">
      <span><svg width="8" height="8" viewBox="0 0 8 8" aria-hidden="true"><path d="M6 0L1 4l5 4z" fill="#777"/></svg></span>
      <span><svg width="8" height="8" viewBox="0 0 8 8" aria-hidden="true"><path d="M2 0l5 4-5 4z" fill="#777"/></svg></span>
    </div>
  </section>

  <div class="abs style-btn">Choose by Style
    <svg width="11" height="7" viewBox="0 0 11 7" aria-hidden="true"><path d="M0 0h11L5.5 7z" fill="#fff"/></svg>
  </div>

  <!-- row 1 -->
  <div class="abs card" style="left:133px;top:563px"><div class="shot shot-black" role="img" aria-label="Product photo: black patent slingback stilettos"></div></div>
  <div class="abs card" style="left:349px;top:563px"><div class="shot shot-suede" role="img" aria-label="Product photo: black suede peep-toe slingback pump"></div></div>
  <div class="abs card" style="left:573px;top:563px"><div class="shot shot-gold" role="img" aria-label="Product photo: gold slingback heels with dark toe caps"></div></div>
  <div class="abs card" style="left:795px;top:563px"><div class="shot shot-beige" role="img" aria-label="Product photo: beige slingback heels with black toe caps"></div></div>

  <div class="abs price" style="left:193px;top:720px">$54.00</div>
  <div class="abs price" style="left:409px;top:720px">$54.00</div>
  <div class="abs price" style="left:633px;top:720px">$54.00</div>
  <div class="abs price" style="left:855px;top:720px">$54.00</div>

  <a class="abs action" href="#" style="left:132px;top:762px">Details</a><a class="abs action" href="#" style="left:258px;top:762px">Add Cart</a>
  <a class="abs action" href="#" style="left:348px;top:762px">Details</a><a class="abs action" href="#" style="left:475px;top:762px">Add Cart</a>
  <a class="abs action" href="#" style="left:572px;top:762px">Details</a><a class="abs action" href="#" style="left:698px;top:762px">Add Cart</a>
  <a class="abs action" href="#" style="left:794px;top:762px">Details</a><a class="abs action" href="#" style="left:920px;top:762px">Add Cart</a>

  <!-- row 2 -->
  <div class="abs card" style="left:132px;top:819px"><div class="shot shot-black" role="img" aria-label="Product photo: black patent slingback stilettos"></div></div>
  <div class="abs card" style="left:348px;top:819px"><div class="shot shot-suede" role="img" aria-label="Product photo: black suede peep-toe slingback pump"></div></div>
  <div class="abs card" style="left:572px;top:819px"><div class="shot shot-gold" role="img" aria-label="Product photo: gold slingback heels with dark toe caps"></div></div>
  <div class="abs card" style="left:794px;top:819px"><div class="shot shot-beige" role="img" aria-label="Product photo: beige slingback heels with black toe caps"></div></div>

  <div class="abs price" style="left:192px;top:976px">$54.00</div>
  <div class="abs price" style="left:408px;top:976px">$54.00</div>
  <div class="abs price" style="left:632px;top:976px">$54.00</div>
  <div class="abs price" style="left:854px;top:976px">$54.00</div>

  <a class="abs action" href="#" style="left:131px;top:1018px">Details</a><a class="abs action" href="#" style="left:257px;top:1018px">Add Cart</a>
  <a class="abs action" href="#" style="left:347px;top:1018px">Details</a><a class="abs action" href="#" style="left:474px;top:1018px">Add Cart</a>
  <a class="abs action" href="#" style="left:571px;top:1018px">Details</a><a class="abs action" href="#" style="left:697px;top:1018px">Add Cart</a>
  <a class="abs action" href="#" style="left:793px;top:1018px">Details</a><a class="abs action" href="#" style="left:919px;top:1018px">Add Cart</a>
</main>

<footer>
  <div class="abs footer-rule"></div>
  <nav class="abs foot-links"><div>Home</div><div>About us</div><div>Store</div><div>Contact us</div></nav>

  <div class="abs foot-head" style="left:348px;top:1074px">Newsletter Subscribe</div>
  <div class="abs newsletter-input"></div>
  <div class="abs subscribe">Subscribe</div>

  <div class="abs foot-head" style="left:581px;top:1074px">We Accept</div>
  <div class="abs payments">
    <span><i></i>Cardix</span><span><i></i>Veltra</span><span><i></i>Pursely</span><span><i></i>Axmoro</span>
  </div>

  <div class="abs foot-head" style="left:781px;top:1074px">Follow Us On</div>
  <div class="abs social">
    <span><i></i>Chirpa</span><span><i></i>Folio</span><span><i></i>Tubely</span><span><i></i>Pinly</span><span><i></i>Tumbla</span><span><i style="border-radius:3px"></i>Mail</span>
  </div>

  <div class="abs legal">© 2012 brr-ivo.<span></span><span></span>Shoe Care<span>/</span>Shoe Size Chart<span>/</span>Terms and Conditions<span>/</span>FREE Shipping and Returns</div>
</footer>

</body>
</html>
```